New Website for IT Services Business

We need an uncoded web design for a new company based in Australia called "Falcon IT". We offer specialised point of sale (POS) support to the hospitality industry. We already support hundreds of cafes and restaurants. We are also about to launch and promote a range of new services with the offering of General IT Support being the most important. Other additional services to be offered are Falcon Vault Storage, reselling and supporting Corvel Shieldware and Trelmo Suite.

We have a logo design and our colour scheme is based on the logo with the addition of charcoal grey (see attached logos). We want the pages to reflect precision and efficiency with sharp characteristics. It must be professional but playful/fun elements are encouraged.

Our target audience is restaurant and cafe owners who are interested in finding high quality POS and IT support for their business.

The main call to action on the home page should be either 'Let's Meet For Coffee!' or 'Find out more (by completing a form)'. If you are unsure about what the general text should say then you can use 'Lorem Ipsum' where required.

The site must be viewable at different resolutions and on smart phones and tablets.

The website structure will be quite simple. We require:
- one impressive landing page. Visitors will quickly determine our services and that we provide a very high level of service while also offering value for money. Obviously a clear list of links (however/wherever you like) to the other pages.
- Simple pages with a similar layout for the following:
- Services - "POS & IT Support for the Hospitality Industry" being the main one. With complementary services also listed. Another call to action on this page with the option of 'Let's Meet For Coffee' or a "More information/Pricing" form to be completed by the visitor.
- Products - will be a small online storefront for a few simple products.
- About - Business background. 2x Directors with a photo and brief Bio.
- Downloads - A list of free files to download. Includes remote access client software.
- Contact Us - Mailing address, Email addresses and Support phone number.

Please feel free to ask any questions about the design. I will assist as much as possible.

Thank you for viewing. We promise to give constructive feedback to every person who submits a design. Thank you so much.

Target Market(s)

Restaurant and Cafe owners.

Industry/Entity Type

Hospitality

Requirements
Must have
• - Viewable on different resolutions and on smart phones and tablets.
- Clear call to action of EITHER 'Let's Meet For Coffee' or a "More information/Pricing" form to be completed by the visitor.

```html
<!DOCTYPE html>
<html lang="en">
<head>
<meta charset="utf-8">
<title>Falcon IT</title>
<link href="https://fonts.googleapis.com/css2?family=Oswald:wght@300;400;500;700&family=Arimo:wght@400;700&display=swap" rel="stylesheet">
<style>
  :root {
    --red: #b01c2e;
    --red-dark: #7a1020;
    --charcoal: #333333;
    --black: #000000;
    --white: #ffffff;
    --panel: #e6e6e6;
    --panel-light: #f4f4f4;
    --text: #444444;
    --field-border: #c8c8c8;
  }
  * { box-sizing: border-box; margin: 0; padding: 0; }
  html, body { width: 1200px; height: 868px; overflow: hidden; background: var(--black); }
  body { position: relative; font-family: "Arimo", Arial, sans-serif; color: var(--text); }

  .hero-backdrop {
    position: absolute; left: 0; top: 0; width: 1200px; height: 604px;
    background: linear-gradient(180deg, #8c1524 0%, #a81d2f 45%, #9a1a2b 100%);
  }
  .call-tab { position: absolute; left: 580px; top: 0; width: 620px; height: 40px; }
  .call-tab span {
    position: absolute; left: 216px; top: 5px; color: var(--white);
    font: 700 15px "Arimo", Arial, sans-serif;
  }

  .brand { position: absolute; left: 92px; top: 90px; display: flex; align-items: center; gap: 22px; }
  .brand-dot { width: 64px; height: 64px; border-radius: 50%; background: var(--white); }
  .brand-name { font: 700 46px/1 "Oswald", sans-serif; color: var(--white); letter-spacing: -1px; }

  .main-nav {
    position: absolute; left: 100px; top: 171px; width: 1002px; height: 31px;
    background: linear-gradient(180deg, #f2f2f2, #d2d2d2);
  }
  .main-nav .home-tab { position: absolute; left: 0; top: 0; }
  .main-nav ul { list-style: none; position: absolute; right: 0; top: 0; display: flex; }
  .main-nav li { font: 400 20px/31px "Oswald", sans-serif; color: var(--black); text-transform: uppercase; }
  .main-nav li:nth-child(1) { margin-right: 62px; }
  .main-nav li:nth-child(2) { margin-right: 53px; }
  .main-nav li:nth-child(3) { margin-right: 48px; }
  .main-nav li:nth-child(4) { margin-right: 33px; }

  .hero { position: absolute; left: 100px; top: 202px; width: 1002px; height: 298px;
    background: linear-gradient(90deg, #eeeeee, #d9d9d9); overflow: hidden; }
  .hero-photo { position: absolute; left: 0; top: 0; width: 660px; height: 298px;
    background: linear-gradient(90deg, #9a7c66 0%, #c9b6a6 40%, #ddd6d0 80%, rgba(230,230,230,0) 100%); }
  .bubbles { position: absolute; left: 0; top: 0; }
  .hero h1 { position: absolute; left: 578px; top: 36px; font: 400 50px/1 "Oswald", sans-serif;
    color: var(--black); letter-spacing: -1px; }

  .coffee-form .field { position: absolute; background: var(--white); border: 1px solid var(--field-border);
    border-radius: 4px; font: 11px "Arimo", Arial, sans-serif; color: #222; padding: 9px 7px; }
  .submit-btn { position: absolute; left: 866px; top: 239px; width: 77px; height: 31px; border-radius: 4px;
    background: var(--red); color: var(--white); font: 500 19px/31px "Oswald", sans-serif; text-align: center; }

  .welcome { position: absolute; left: 100px; top: 527px; width: 1002px; height: 196px;
    border-radius: 14px; background: linear-gradient(180deg, var(--panel-light), var(--panel)); border: 1px solid #bbb; overflow: hidden; }
  .welcome-band { position: absolute; left: 0; top: 20px; width: 100%; height: 62px; background: var(--charcoal);
    border-top: 2px solid #aaa; border-bottom: 2px solid #aaa; }
  .welcome-band h2 { font: 400 40px/58px "Oswald", sans-serif; color: var(--white); padding-left: 14px; letter-spacing: -0.5px; }

  .col { position: absolute; top: 94px; }
  .col h3 { font: 400 23px/1 "Oswald", sans-serif; color: var(--red); text-transform: uppercase; }
  .about { left: 20px; width: 500px; }
  .about p { font-size: 11.4px; line-height: 14.6px; margin-top: 6px; text-align: justify; }
  .divider { position: absolute; top: 94px; width: 1px; height: 82px; background: #b5b5b5; }
  .offer { left: 578px; width: 200px; }
  .offer h3 { padding-left: 14px; }
  .why { left: 806px; width: 190px; }
  .why h3 { padding-left: 18px; }
  .col ul { list-style: none; margin-top: 6px; }
  .col li { font-size: 12px; line-height: 14.5px; display: flex; align-items: center; gap: 5px; }
  .col li::before { content: ""; width: 6px; height: 6px; border: 2px solid #666; border-radius: 50%; background: #eee; }
  .why li { gap: 9px; }
  .learn-more { position: absolute; left: 716px; top: 177px; font: 700 11px "Arimo", Arial, sans-serif; color: var(--red); }

  .site-footer { position: absolute; left: 0; top: 730px; width: 1200px; color: var(--white); }
  .footer-block { position: absolute; top: 10px; }
  .footer-block h4 { font: 700 12px "Arimo", Arial, sans-serif; margin-bottom: 2px; }
  .contact { left: 121px; font-size: 12.5px; line-height: 16.8px; }
  .services { left: 327px; font-size: 11px; line-height: 13px; }
  .follow { position: absolute; left: 880px; top: 52px; display: flex; align-items: center; gap: 11px; }
  .follow span { font: 700 12px "Arimo", Arial, sans-serif; margin-right: 2px; }
  .follow i { width: 34px; height: 34px; border-radius: 50%; background: #2b2b2b; display: block; }
  .footer-rule { position: absolute; left: 0; top: 110px; width: 1200px; height: 1px; background: #2a2a2a; }
  .copyright { position: absolute; right: 110px; top: 118px; font-size: 11px; }
</style>
</head>
<body>
  <div class="hero-backdrop" role="img" aria-label="Red-tinted photograph of a street cafe terrace with palms"></div>

  <svg class="call-tab" viewBox="0 0 620 40" aria-hidden="true">
    <path d="M0 0 H620 V0 C520 18 400 32 300 34 C180 36 90 20 0 0Z" fill="#ffffff"/>
    <path d="M14 0 H620 V0 C520 12 400 26 300 28 C180 30 100 16 14 0Z" fill="#000000"/>
  </svg>
  <div class="call-tab"><span>Call us at&nbsp; 0-000-000-0000</span></div>

  <div class="brand">
    <div class="brand-dot"></div>
    <div class="brand-name">Falcon IT</div>
  </div>

  <nav class="main-nav">
    <svg class="home-tab" width="52" height="31" viewBox="0 0 52 31" aria-label="Home">
      <path d="M0 0 H36 L50 15.5 L36 31 H0Z" fill="#000"/>
      <path d="M11 15 L17 9.5 L23 15 H21 V21 H18.5 V17.5 H15.5 V21 H13 V15Z" fill="#fff"/>
    </svg>
    <ul>
      <li>Home</li>
      <li>What We Are</li>
      <li>What We Offer</li>
      <li>Contact Us</li>
    </ul>
  </nav>

  <section class="hero">
    <div class="hero-photo" role="img" aria-label="Photograph of two business people meeting over coffee and a laptop in a cafe"></div>
    <svg class="bubbles" width="1002" height="298" viewBox="0 0 1002 298" aria-hidden="true">
      <ellipse cx="665" cy="26" rx="22" ry="14" fill="#b01c2e"/>
      <path d="M652 36 L655 46 L664 38Z" fill="#b01c2e"/>
      <ellipse cx="583" cy="142" rx="34" ry="18" fill="#b01c2e"/>
      <path d="M600 155 L605 172 L590 158Z" fill="#b01c2e"/>
      <ellipse cx="720" cy="253" rx="52" ry="28" fill="#b01c2e"/>
      <path d="M705 278 L700 288 L725 280Z" fill="#b01c2e"/>
    </svg>
    <h1>Let’s Meet For Coffee’</h1>
    <form class="coffee-form">
      <div class="field" style="left:582px;top:113px;width:181px;height:31px;">Name</div>
      <div class="field" style="left:770px;top:113px;width:181px;height:31px;">Contact No.</div>
      <div class="field" style="left:582px;top:154px;width:181px;height:31px;">Email</div>
      <div class="field" style="left:771px;top:154px;width:181px;height:70px;">Message</div>
      <div class="field" style="left:584px;top:194px;width:181px;height:31px;">Address</div>
      <div class="submit-btn">Submit</div>
    </form>
  </section>

  <section class="welcome">
    <div class="welcome-band"><h2>Welcome To Falcon IT</h2></div>
    <div class="col about">
      <h3>Little About Falcon</h3>
      <p>We offer specialised point of sale (POS) support to the hospitality industry. We already support hundreds of cafes and restaurants. We are also about to launch and promote a range of new services with the offering of General IT Support being the most important. Other additional services to be offered are Falcon Vault Storage, reselling and supporting Corvel Shieldware..</p>
    </div>
    <div class="divider" style="left:536px"></div>
    <div class="col offer">
      <h3>What We Offer</h3>
      <ul>
        <li>What we offer heading 1</li>
        <li>What we offer heading 2</li>
        <li>What we offer heading 3</li>
      </ul>
    </div>
    <div class="divider" style="left:782px"></div>
    <div class="col why">
      <h3>Why Choose Us</h3>
      <ul>
        <li>Why choose us heading 1</li>
        <li>Why choose us heading 2</li>
        <li>Why choose us heading 3</li>
      </ul>
    </div>
    <div class="learn-more">Learn More</div>
  </section>

  <footer class="site-footer">
    <div class="footer-block contact">
      <h4>CONTACT US</h4>
      xxxxxxxxxxxxxxxxxxxxxx<br>
      xxxxxxxxxxxxxxxxxxxxxx<br>
      xxxxxxxxxxxxxxxxxxxxxx<br>
      phone: 000-0000-000<br>
      email:info@falconit.com
    </div>
    <div class="footer-block services">
      <h4>SERVICES</h4>
      Services Title 1<br>
      Services Title 2<br>
      Services Title 3<br>
      Services Title 4<br>
      Services Title 5
    </div>
    <div class="follow">
      <span>Follow Us On</span>
      <i></i><i></i><i></i>
    </div>
    <div class="footer-rule"></div>
    <div class="copyright">Copyright 2012. All rights reserved.</div>
  </footer>
</body>
</html>
```